New Business Card

Would like a shiny card with Metallic logo raised on th front. Address 518 Whitlock Avenue, Toronto Ontario M4K2J8, phone 416 555 0182, email kvbe@lindenmail.ca and web www.kvbe.ca on the back in right and left lower corners balanced. Top of back should say Personalized Care for Pet's and their People centered. Leaving space on the back to write. Horizontal placement

Industry/Entity Type

Business

```html
<!DOCTYPE html>
<html lang="en">
<head>
<meta charset="utf-8">
<title>Kingsview Bay Animal Hospital — Business Card</title>
<link href="https://fonts.googleapis.com/css2?family=Roboto:wght@400;500;700&display=swap" rel="stylesheet">
<style>
  :root {
    --backdrop: #ebebe9;
    --card: #f7f7f5;
    --card-edge: #e2e2df;
    --ink: #8c8c8c;
    --ink-strong: #7d7d7d;
    --rule: #9a9a9a;
    --metal-light: #d8d8d8;
    --metal-dark: #9e9e9e;
  }
  * { margin: 0; padding: 0; box-sizing: border-box; }
  html, body {
    width: 966px;
    height: 1200px;
    overflow: hidden;
    background: var(--backdrop);
    font-family: "Roboto", Arial, sans-serif;
    color: var(--ink);
  }
  .canvas {
    position: relative;
    width: 966px;
    height: 1200px;
  }
  .card {
    position: absolute;
    left: 204px;
    width: 552px;
    height: 342px;
    background: var(--card);
    border: 1px solid var(--card-edge);
    box-shadow: 0 2px 6px rgba(0, 0, 0, 0.08);
  }
  .card--front { top: 136px; }
  .card--back { top: 771px; }

  /* Front */
  .brand {
    position: absolute;
    left: 0;
    right: 0;
    top: 48px;
    text-align: center;
  }
  .brand__dot {
    display: block;
    width: 58px;
    height: 58px;
    margin: 0 auto 14px;
    border-radius: 50%;
    background: linear-gradient(160deg, var(--metal-light), var(--metal-dark));
  }
  .brand__name {
    font-size: 22px;
    font-weight: 400;
    letter-spacing: 2px;
    line-height: 1.15;
    color: var(--ink-strong);
    text-transform: uppercase;
  }
  .person {
    position: absolute;
    left: 68px;
    top: 234px;
    width: 170px;
    text-align: right;
  }
  .person__name {
    font-size: 19px;
    font-weight: 700;
    color: var(--ink-strong);
    line-height: 1.1;
  }
  .person__role {
    font-size: 14px;
    font-weight: 500;
    line-height: 1.3;
  }
  .contact {
    position: absolute;
    left: 259px;
    top: 222px;
    font-size: 13.5px;
    line-height: 16px;
    list-style: none;
  }
  .contact__gap { margin-top: 6px; }

  /* Back */
  .tagline {
    position: absolute;
    left: 0;
    right: 0;
    top: 48px;
    text-align: center;
    font-size: 13px;
    font-weight: 500;
    text-transform: uppercase;
  }
  .writing-lines {
    position: absolute;
    left: 46px;
    top: 98px;
    width: 466px;
  }
  .writing-lines__rule {
    height: 1px;
    background: var(--rule);
    margin-bottom: 59px;
  }
</style>
</head>
<body>
<main class="canvas">
  <section class="card card--front" aria-label="Card front">
    <div class="brand">
      <span class="brand__dot"></span>
      <p class="brand__name">Kingsview Bay<br>Animal Hospital</p>
    </div>
    <div class="person">
      <p class="person__name">MARK ELLISON</p>
      <p class="person__role">CEO/FOUNDER</p>
    </div>
    <ul class="contact">
      <li>518 Whitlock Avenue</li>
      <li>Toronto Ontario M4K2J8</li>
      <li class="contact__gap">416 555 0182</li>
      <li>kvbe@lindenmail.ca</li>
      <li>www.kvbe.ca</li>
    </ul>
  </section>

  <section class="card card--back" aria-label="Card back">
    <p class="tagline">Personalized care for pet's and their people</p>
    <div class="writing-lines">
      <div class="writing-lines__rule"></div>
      <div class="writing-lines__rule"></div>
      <div class="writing-lines__rule"></div>
      <div class="writing-lines__rule"></div>
    </div>
  </section>
</main>
</body>
</html>
```